'Lanterns' CD cover project

I am recording a new album 'Lanterns' and need a CD cover design. No design specs, but I want something simple and classy. My name (Marek Townley) does not necessarily have to appear on the cover, and it does not have to relate to my previous 11 albums. I have posted some of my own ideas on Snapwall.

Target Market(s)

I have an established 50s+ fan base, but am seeking to appeal to a younger more modern audience.

Font styles to use
Other font styles liked:
• Yu Gothic Light but open to suggestions.

Colors

Designer to choose colors to be used in the design.

Requirements
Must have
• Simple, clean, classy, Im open to a photo image or simply a graphic design.
Nice to have
• Modern (pastel?) colors.. if pastels are modern?!
Should not have
• Nothing 'In Yer Face'. Prefer sublte, nuance, classy, tasteful, clean lines, unusual font.

```html
<!DOCTYPE html>
<html lang="en">
<head>
<meta charset="utf-8">
<title>Lanterns — Marek Townley</title>
<link rel="stylesheet" href="https://fonts.googleapis.com/css2?family=Montserrat:wght@400;500&display=swap">
<style>
  :root {
    --page-bg: #f5f5f5;
    --sky-top: #c9cde6;
    --sky-low: #dfe3ef;
    --horizon-green: #a9c96a;
    --marsh-green: #7fb43c;
    --forest-green: #4f8e24;
    --deep-green: #2f6a17;
    --river-blue: #3a4f78;
    --type-light: #eef0f7;
  }

  * { box-sizing: border-box; margin: 0; padding: 0; }

  html, body {
    width: 1200px;
    height: 1000px;
    overflow: hidden;
    background: var(--page-bg);
  }

  .canvas {
    position: relative;
    width: 1200px;
    height: 1000px;
    display: flex;
    align-items: center;
    justify-content: center;
  }

  .album-cover {
    position: relative;
    width: 760px;
    height: 760px;
    overflow: hidden;
  }

  .cover-photo {
    position: absolute;
    inset: 0;
    background:
      linear-gradient(180deg,
        var(--sky-top) 0%,
        var(--sky-low) 12%,
        var(--horizon-green) 14%,
        var(--marsh-green) 30%,
        var(--river-blue) 46%,
        var(--marsh-green) 56%,
        var(--forest-green) 72%,
        var(--deep-green) 100%);
  }

  .album-title {
    position: absolute;
    left: 0;
    right: 0;
    top: 49%;
    transform: translateY(-50%);
    text-align: center;
    font-family: "Montserrat", sans-serif;
    font-weight: 400;
    font-size: 62px;
    letter-spacing: 0.55em;
    padding-left: 0.55em;
    color: var(--type-light);
    text-transform: uppercase;
  }

  .artist-name {
    position: absolute;
    left: 0;
    right: 0;
    bottom: 52px;
    text-align: center;
    font-family: "Montserrat", sans-serif;
    font-weight: 500;
    font-size: 17px;
    letter-spacing: 0.55em;
    padding-left: 0.55em;
    color: var(--type-light);
    text-transform: uppercase;
  }
</style>
</head>
<body>
  <main class="canvas">
    <section class="album-cover">
      <div class="cover-photo" role="img" aria-label="Aerial photograph of a winding blue river meandering through green mangrove wetlands under a pale hazy sky"></div>
      <h1 class="album-title">Lanterns</h1>
      <p class="artist-name">Marek Townley</p>
    </section>
  </main>
</body>
</html>
```